Bref créative
Stationery
Health centre
Bright & Fun-filled
Meadowlark Wellness Studio
We need cards for different individuals - easily editable
12B Harlow Terrace
Edinburgh
EH4 7QN
info@meadowlarkwellstudio.co.uk
www.meadowlarkwellstudio.co.uk
appointments date and time & cancelation policy.
We require 24 hours cancellation for appointments otherwise a charge may be incurred.

```html
<!DOCTYPE html>
<html lang="en">
<head>
<meta charset="utf-8">
<title>Meadowlark Wellness Studio – Business and Appointment Cards</title>
<link rel="stylesheet" href="https://fonts.googleapis.com/css2?family=Crimson+Text:wght@400;600&display=swap">
<style>
  :root {
    --backdrop: #e4e2de;
    --card: #ffffff;
    --ink: #2f2f2f;
    --muted: #555555;
    --brand-green: #5f8f2e;
    --rule: #9a9a9a;
  }
  * { box-sizing: border-box; margin: 0; padding: 0; }
  html, body { width: 1200px; height: 490px; overflow: hidden; }
  body {
    background: var(--backdrop);
    font-family: "Crimson Text", Georgia, serif;
    color: var(--ink);
    position: relative;
  }
  .card {
    position: absolute;
    top: 125px;
    width: 420px;
    height: 260px;
    background: var(--card);
    border-radius: 18px;
    box-shadow: 0 3px 10px rgba(0,0,0,0.18);
  }
  .card--front { left: 172px; }
  .card--back { left: 612px; }

  /* Front */
  .brand {
    position: absolute;
    top: 22px; left: 0; right: 0;
    display: flex; align-items: center; justify-content: center; gap: 8px;
  }
  .brand__dot {
    width: 12px; height: 12px; border-radius: 50%;
    background: var(--brand-green);
  }
  .brand__name {
    font-size: 22px; font-weight: 600; color: var(--brand-green);
    letter-spacing: 0.3px;
  }
  .holder { position: absolute; left: 38px; top: 118px; }
  .holder__name { font-size: 14px; line-height: 16px; }
  .holder__role { font-size: 9px; line-height: 11px; color: var(--muted); }

  .contact-block {
    position: absolute; left: 38px; top: 168px;
    display: flex; align-items: stretch; gap: 9px;
  }
  .address {
    font-style: normal;
    font-size: 13.5px; line-height: 17px;
    white-space: nowrap;
  }
  .divider { width: 1px; background: var(--rule); }
  .contact {
    font-size: 13px; line-height: 17px;
    display: grid; grid-template-columns: 38px auto;
    white-space: nowrap;
  }
  .contact__label { color: var(--brand-green); }

  /* Back */
  .brand--small {
    top: 24px; left: auto; right: 30px; justify-content: flex-end; gap: 5px;
  }
  .brand--small .brand__dot { width: 8px; height: 8px; }
  .brand--small .brand__name { font-size: 12px; }

  .appointment { position: absolute; left: 24px; top: 52px; font-size: 13px; }
  .appointment__name-line {
    width: 190px; border-bottom: 1px solid var(--ink); height: 16px;
  }
  .appointment__label { margin-top: 2px; }
  .appointment__when { margin-top: 22px; display: flex; align-items: baseline; gap: 6px; }
  .blank { display: inline-block; border-bottom: 1px solid var(--ink); height: 12px; }
  .blank--date { width: 72px; }
  .blank--time { width: 72px; }

  .days { margin-top: 24px; display: flex; gap: 14px; font-size: 13px; }
  .day { display: flex; align-items: center; gap: 3px; }
  .day__box { width: 9px; height: 9px; border: 1px solid var(--ink); }

  .policy {
    position: absolute; left: 24px; right: 24px; top: 197px;
    font-size: 9.5px; line-height: 12px;
  }
  .policy__title { font-weight: 600; }
</style>
</head>
<body>
  <section class="card card--front" aria-label="Business card front">
    <div class="brand">
      <span class="brand__dot"></span>
      <span class="brand__name">Meadowlark Wellness Studio</span>
    </div>
    <div class="holder">
      <p class="holder__name">Wellness Studio</p>
      <p class="holder__role">CEO</p>
    </div>
    <div class="contact-block">
      <address class="address">
        12B Harlow Terrace<br>Edinburgh<br>EH4 7QN
      </address>
      <div class="divider"></div>
      <div class="contact">
        <span class="contact__label">Phone</span><span>: 0131 555 0192</span>
        <span class="contact__label">Email</span><span>: info@meadowlarkwellstudio.co.uk</span>
        <span class="contact__label">Web</span><span>: www.meadowlarkwellstudio.co.uk</span>
      </div>
    </div>
  </section>

  <section class="card card--back" aria-label="Appointment card">
    <div class="brand brand--small">
      <span class="brand__dot"></span>
      <span class="brand__name">Meadowlark Wellness Studio</span>
    </div>
    <div class="appointment">
      <div class="appointment__name-line"></div>
      <p class="appointment__label">has an appointment on</p>
      <p class="appointment__when">Date: <span class="blank blank--date"></span> at <span class="blank blank--time"></span> AM / PM</p>
      <div class="days">
        <span class="day"><span class="day__box"></span>Mon</span>
        <span class="day"><span class="day__box"></span>Tues</span>
        <span class="day"><span class="day__box"></span>Wed</span>
        <span class="day"><span class="day__box"></span>Thu</span>
        <span class="day"><span class="day__box"></span>Fri</span>
        <span class="day"><span class="day__box"></span>Sat</span>
      </div>
    </div>
    <div class="policy">
      <p class="policy__title">Cancellation Policy:</p>
      <p>We require 24 hours cancellation for appointments otherwise a charge may be incurred.</p>
    </div>
  </section>
</body>
</html>
```